Professional Sales Business looking for inspirational poster

I need an inspirational poster design for sales professionals, targeted around the phrase "Win Fast, Lose Fast". The style of the poster will be primarily minimalistic and flat with the main focus being on the phrase, however, any graphics or creative font and background styles are encouraged. Color choice is up to you.

Design Specs:
Vector files are best. If creating a vector file isn't possible, 150dpi raster images (at actual size or bigger) are good too. The poster must be in a portrait layout and scalable to the sizes of 18" X 24" and 24" X 36". Please convert all text to outlines.

Please msg me if you have any additional questions.

```html
<!DOCTYPE html>
<html lang="en">
<head>
<meta charset="utf-8">
<title>Win Fast, Lose Fast</title>
<link href="https://fonts.googleapis.com/css2?family=Marcellus+SC&display=swap" rel="stylesheet">
<style>
  :root {
    --paper: #bcbcbc;
    --band: #9c9c9c;
    --ink: #000000;
  }
  html, body {
    margin: 0;
    padding: 0;
    width: 778px;
    height: 1200px;
    overflow: hidden;
    background: var(--paper);
  }
  .poster {
    display: block;
    width: 778px;
    height: 1200px;
  }
  .poster__paper { fill: var(--paper); }
  .poster__side-band,
  .poster__stripe { fill: var(--band); }
  .poster__divider { fill: var(--ink); }
  .slogan {
    font-family: "Marcellus SC", "Cinzel", serif;
    font-size: 118px;
    fill: var(--ink);
  }
  .thumb-icon { fill: var(--ink); }
</style>
</head>
<body>
<svg class="poster" viewBox="0 0 778 1200" xmlns="http://www.w3.org/2000/svg" role="img" aria-label="Win Fast, Lose Fast poster">
  <rect class="poster__paper" x="0" y="0" width="778" height="1200"/>
  <rect class="poster__side-band" x="0" y="0" width="50" height="1200"/>

  <g class="poster__stripes poster__stripes--top">
    <rect class="poster__stripe" x="50" y="120" width="728" height="12"/>
    <rect class="poster__stripe" x="50" y="150" width="728" height="11"/>
    <rect class="poster__stripe" x="50" y="182" width="728" height="8"/>
    <rect class="poster__stripe" x="50" y="208" width="728" height="11"/>
  </g>

  <g class="poster__stripes poster__stripes--bottom">
    <rect class="poster__stripe" x="50" y="973" width="728" height="16"/>
    <rect class="poster__stripe" x="50" y="1006" width="728" height="7"/>
    <rect class="poster__stripe" x="50" y="1035" width="728" height="11"/>
    <rect class="poster__stripe" x="50" y="1065" width="728" height="11"/>
  </g>

  <text class="slogan slogan--win" x="145" y="531" textLength="402" lengthAdjust="spacingAndGlyphs">Win Fast</text>
  <path class="thumb-icon thumb-icon--up"
        d="M590 530 L593 488 Q596 462 601 440 L604 420 Q607 414 610 420 L612 440 L611 464
           L628 463 Q634 464 633 471 Q640 472 639 480 Q644 482 642 492 Q646 496 643 504
           Q646 510 641 516 Q642 524 634 526 L612 527 Z"/>

  <rect class="poster__divider" x="50" y="592" width="728" height="3"/>

  <text class="slogan slogan--lose" x="157" y="735" textLength="380" lengthAdjust="spacingAndGlyphs">Lose Fast</text>
  <path class="thumb-icon thumb-icon--down"
        d="M584 682 L631 681 Q640 682 639 690 Q645 694 642 702 Q647 706 643 714
           Q646 720 641 726 Q643 734 636 736 L620 737 L621 758 Q624 772 628 782 L624 788
           Q618 770 612 758 Q602 748 592 740 L586 736 Z"/>
</svg>
</body>
</html>
```